Fallow Crest Bourbon Barrel Aged Wine

We are taking a sweet red wine and barrel aging it in previously used bourbon barrels. The abv is 16%. Kentucky based. I have attached our Brand logo for reference. Use colors that evoke warmth, richness, and sophistication. We would like to consider a raised or textured label.

Target Market(s)

bourbon and wine drinkers

```html
<!DOCTYPE html>
<html lang="en">
<head>
<meta charset="utf-8">
<title>Fallow Crest Distillery – Cabernet Sauvignon Label</title>
<link rel="stylesheet" href="https://fonts.googleapis.com/css2?family=Cinzel:wght@400;500;600&family=EB+Garamond:wght@400;500;600&display=swap">
<style>
  :root {
    --page: #ffffff;
    --label: #252525;
    --gold: #cdb564;
    --gold-deep: #c8911f;
    --ivory: #ffffff;
  }
  * { margin: 0; padding: 0; box-sizing: border-box; }
  html, body {
    width: 757px;
    height: 1200px;
    overflow: hidden;
    background: var(--page);
  }
  .label {
    position: relative;
    width: 757px;
    height: 1200px;
  }
  .label-frame {
    position: absolute;
    inset: 0;
    width: 757px;
    height: 1200px;
  }
  .emblem-area {
    position: absolute;
    left: 248px;
    top: 122px;
    width: 244px;
    height: 182px;
    border-radius: 12px;
    background: radial-gradient(ellipse at 50% 45%, #b8871f 0%, #7a5d1f 60%, #3a3124 100%);
  }
  .label-text {
    position: absolute;
    left: 0;
    width: 100%;
    text-align: center;
    color: var(--ivory);
    white-space: nowrap;
  }
  .brand-name {
    top: 314px;
    font-family: "Cinzel", serif;
    font-weight: 600;
    font-size: 75px;
    letter-spacing: 1px;
    line-height: 1;
  }
  .brand-sub {
    top: 387px;
    font-family: "Cinzel", serif;
    font-weight: 600;
    font-size: 34px;
    letter-spacing: 4px;
    line-height: 1;
  }
  .varietal-art {
    position: absolute;
    left: 268px;
    top: 482px;
    width: 180px;
    height: 400px;
    border-radius: 90px 90px 60px 60px;
    background: radial-gradient(ellipse at 50% 45%, #7e7045 0%, #4f4832 55%, #2f2d27 100%);
  }
  .varietal {
    top: 908px;
    font-family: "Cinzel", serif;
    font-weight: 500;
    font-size: 52px;
    letter-spacing: 0;
    line-height: 1;
  }
  .aging {
    top: 985px;
    font-family: "EB Garamond", serif;
    font-weight: 500;
    font-size: 26px;
    letter-spacing: 0.5px;
    line-height: 1;
  }
  .vintage {
    top: 1019px;
    font-family: "EB Garamond", serif;
    font-weight: 400;
    font-size: 38px;
    letter-spacing: 1px;
    font-variant-numeric: oldstyle-nums;
    line-height: 1;
  }
  .origin {
    top: 1103px;
    left: -6px;
    font-family: "EB Garamond", serif;
    font-weight: 500;
    font-size: 22px;
    letter-spacing: 0.3px;
    line-height: 1;
  }
  .abv {
    position: absolute;
    top: 1103px;
    left: 656px;
    color: var(--ivory);
    font-family: "EB Garamond", serif;
    font-size: 22px;
    font-variant-numeric: oldstyle-nums;
    line-height: 1;
  }
</style>
</head>
<body>
<main class="label">
  <svg class="label-frame" viewBox="0 0 757 1200" aria-hidden="true">
    <defs>
      <linearGradient id="rule-taper" x1="0" x2="1" y1="0" y2="0">
        <stop offset="0" stop-color="var(--gold-deep)" stop-opacity="0"/>
        <stop offset="0.15" stop-color="var(--gold-deep)"/>
        <stop offset="0.85" stop-color="var(--gold-deep)"/>
        <stop offset="1" stop-color="var(--gold-deep)" stop-opacity="0"/>
      </linearGradient>
      <linearGradient id="rule-pale" x1="0" x2="1" y1="0" y2="0">
        <stop offset="0" stop-color="var(--gold)" stop-opacity="0"/>
        <stop offset="0.2" stop-color="var(--gold)"/>
        <stop offset="0.8" stop-color="var(--gold)"/>
        <stop offset="1" stop-color="var(--gold)" stop-opacity="0"/>
      </linearGradient>
    </defs>
    <path d="M4 1196 V378.5 A374.5 374.5 0 0 1 753 378.5 V1196 Z" fill="var(--label)" stroke="var(--gold)" stroke-width="8"/>
    <path d="M21 1179 V378.5 A357.5 357.5 0 0 1 736 378.5 V1179 Z" fill="none" stroke="var(--gold)" stroke-width="5"/>
    <path d="M33 1167 V378.5 A345.5 345.5 0 0 1 724 378.5 V1167 Z" fill="none" stroke="var(--gold)" stroke-width="1.5"/>
    <rect x="100" y="304" width="545" height="3" fill="url(#rule-taper)"/>
    <rect x="104" y="402" width="148" height="3" fill="url(#rule-taper)"/>
    <rect x="510" y="402" width="132" height="3" fill="url(#rule-taper)"/>
    <rect x="172" y="1035" width="158" height="3" fill="url(#rule-pale)"/>
    <rect x="443" y="1035" width="130" height="3" fill="url(#rule-pale)"/>
  </svg>

  <div class="emblem-area" role="img" aria-label="Brand emblem area in warm gold"></div>

  <h1 class="label-text brand-name">Fallow Crest</h1>
  <p class="label-text brand-sub">Distillery</p>

  <div class="varietal-art" role="img" aria-label="Engraved-style gold illustration of a grape cluster with a vine leaf"></div>

  <h2 class="label-text varietal">Cabernet Sauvignon</h2>
  <p class="label-text aging">BOURBON BARREL AGED</p>
  <p class="label-text vintage">2023</p>
  <p class="label-text origin">MADE IN KENTUCKY</p>
  <p class="abv">16%</p>
</main>
</body>
</html>
```